Letterhead, with compliments slip and business cards

Hi, We would like to redesign our stationary letter heads. We are looking for a new coordination suite of three documents: letter head, with compliments slip and business card designed. We are a primary school catering for Kindergarten to year 6 in the leafy suburbs of a metropolitan area. We are looking for a modern style that reflects the area in which we work. Our school colours are bottle green and white - the same shade of green as in the school logo attached. It would need to include the school logo which I have attached as well as the following information:
WILLOWMERE HEIGHTS PUBLIC SCHOOL
Tamberlin Avenue, Larkfield, WR 3418
Telephone: 02 7316 4859
Coastal Board of Schooling | TEVARN Provider Code: 00731K

```html
<!DOCTYPE html>
<html lang="en">
<head>
<meta charset="utf-8">
<title>Willowmere Heights Public School – Stationery Suite</title>
<link rel="stylesheet" href="https://fonts.googleapis.com/css2?family=Roboto:wght@400;500;700;900&family=Great+Vibes&display=swap">
<style>
  :root{
    --bottle:#1f563b;
    --bottle-dark:#174630;
    --paper:#ffffff;
    --paper-tint:#f6f7f6;
    --ink:#2b2f2d;
    --ink-soft:#5d625f;
    --rule:#9aa39e;
    --backdrop:#eceeed;
  }
  *{box-sizing:border-box;margin:0;padding:0}
  html,body{width:1200px;height:792px;overflow:hidden}
  body{background:var(--backdrop);font-family:"Roboto",Arial,sans-serif;color:var(--ink);position:relative}
  .piece{position:absolute;overflow:hidden;box-shadow:0 2px 6px rgba(0,0,0,.12)}
  .piece svg.shape{position:absolute;left:0;top:0}

  /* School name mark */
  .mark{display:flex;align-items:center;gap:4px;font-weight:700;text-transform:uppercase;line-height:1.05}
  .mark .mark-square{flex:none;display:block}
  .mark.on-green{color:var(--paper)}
  .mark.on-green .mark-square{background:var(--paper)}
  .mark.on-white{color:var(--bottle)}
  .mark.on-white .mark-square{background:var(--bottle)}

  .contact{display:flex;align-items:center;gap:4px;white-space:nowrap}
  .contact svg{flex:none}

  /* Business card front */
  .card-front{left:167px;top:107px;width:157px;height:91px;background:var(--bottle)}
  .card-front .mark{position:absolute;left:0;right:0;top:14px;flex-direction:column;gap:3px;font-size:6px;text-align:center}
  .card-front .mark .mark-square{width:16px;height:16px}
  .card-front .school-name{position:absolute;left:0;right:0;top:60px;text-align:center;color:var(--paper);font-weight:700;font-size:7.2px;letter-spacing:.1px;white-space:nowrap}
  .card-front .board-line{position:absolute;left:0;right:0;top:70px;text-align:center;color:#d5e2da;font-size:3.6px;white-space:nowrap}

  /* Business card back */
  .card-back{left:167px;top:217px;width:157px;height:88px;background:var(--paper-tint)}
  .card-back .holder{position:absolute;left:12px;top:18px}
  .card-back .holder-name{color:var(--bottle);font-weight:900;font-size:9px;line-height:1;white-space:nowrap}
  .card-back .holder-role{color:var(--ink-soft);font-size:4.2px;margin-top:2px}
  .card-back .mark{position:absolute;right:10px;top:10px;font-size:4.4px;flex-direction:column;gap:2px;text-align:center;width:36px}
  .card-back .mark .mark-square{width:12px;height:12px}
  .card-back .contacts{position:absolute;left:10px;top:54px;color:var(--paper);font-size:3.6px;display:flex;flex-direction:column;gap:3px}
  .card-back .card-address{position:absolute;right:8px;top:77px;color:#dbe6df;font-size:3.6px;white-space:nowrap}

  /* Letterhead */
  .letterhead{left:373px;top:104px;width:293px;height:416px;background:var(--paper)}
  .letterhead .mark{position:absolute;left:16px;top:14px;width:40px;flex-direction:column;gap:2px;font-size:4.6px;text-align:center}
  .letterhead .mark .mark-square{width:14px;height:14px}
  .letterhead .masthead{position:absolute;left:60px;top:19px}
  .letterhead .masthead h1{color:var(--bottle);font-weight:900;font-size:10.6px;letter-spacing:.1px;line-height:1;white-space:nowrap}
  .letterhead .masthead p{font-size:4.8px;font-weight:500;color:var(--ink);margin-top:2px;white-space:nowrap}
  .letterhead .head-rule{position:absolute;left:16px;right:16px;top:47px;height:1px;background:var(--rule)}
  .letterhead .head-rule::before{content:"";position:absolute;left:0;top:-1px;width:52px;height:3px;background:var(--bottle)}
  .letterhead .letter-date{position:absolute;right:20px;top:58px;font-size:4.6px;color:var(--ink)}
  .letterhead .letter-body{position:absolute;left:22px;right:22px;top:70px;font-size:4.8px;line-height:1.6;color:var(--ink-soft)}
  .letterhead .letter-body p{margin-bottom:8px}
  .letterhead .signoff{position:absolute;left:22px;top:282px}
  .letterhead .signature{font-family:"Great Vibes",cursive;font-size:12px;color:var(--ink)}
  .letterhead .signer{font-size:5px;font-weight:700;color:var(--ink);margin-top:2px}
  .letterhead .signer-role{font-size:4.4px;color:var(--ink-soft)}
  .letterhead .contacts{position:absolute;left:20px;top:364px;color:var(--paper);font-size:4.2px;display:flex;flex-direction:column;gap:5px}
  .letterhead .footer-board{position:absolute;right:14px;top:364px;color:var(--paper);font-size:3.8px;white-space:nowrap}

  /* Compliments slip */
  .slip{left:719px;top:109px;width:328px;height:164px;background:var(--paper)}
  .slip .mark{position:absolute;left:14px;top:12px;width:46px;flex-direction:column;gap:2px;font-size:5px;text-align:center}
  .slip .mark .mark-square{width:16px;height:16px}
  .slip .write-lines{position:absolute;left:178px;top:11px;width:135px}
  .slip .write-lines span{display:block;height:1px;background:var(--rule);margin-bottom:13px}
  .slip .school-name{position:absolute;left:14px;top:101px;color:var(--paper);font-weight:700;font-size:8px;white-space:nowrap}
  .slip .contacts{position:absolute;left:16px;top:121px;color:var(--paper);font-size:4.4px;display:flex;flex-direction:column;gap:4px}
  .slip .board{position:absolute;right:14px;top:135px;text-align:right;color:var(--paper);font-size:5px;line-height:1.5;white-space:nowrap}

  /* Envelope back */
  .envelope{left:717px;top:351px;width:329px;height:164px;background:var(--paper)}
  .envelope .mark{position:absolute;left:0;right:0;top:58px;flex-direction:column;gap:6px;font-size:9px;text-align:center}
  .envelope .mark .mark-square{width:30px;height:30px}
</style>
</head>
<body>

<!-- Business card: front -->
<section class="piece card-front" aria-label="Business card front">
  <div class="mark on-green"><span class="mark-square"></span>Willowmere Heights</div>
  <div class="school-name">WILLOWMERE HEIGHTS PUBLIC SCHOOL</div>
  <div class="board-line">Coastal Board of Schooling | TEVARN Provider Code: 00731K</div>
</section>

<!-- Business card: back -->
<section class="piece card-back" aria-label="Business card back">
  <svg class="shape" width="157" height="88" viewBox="0 0 157 88" aria-hidden="true">
    <path d="M0,46 H58 C78,46 80,58 100,58 H157 V88 H0 Z" fill="var(--bottle)"/>
  </svg>
  <div class="holder">
    <div class="holder-name">ARLO PENNING</div>
    <div class="holder-role">Principal</div>
  </div>
  <div class="mark on-white"><span class="mark-square"></span>Willowmere Heights</div>
  <div class="contacts">
    <div class="contact"><svg width="4" height="4" viewBox="0 0 10 10"><path d="M5 0a3.6 3.6 0 0 0-3.6 3.6C1.4 6.5 5 10 5 10s3.6-3.5 3.6-6.4A3.6 3.6 0 0 0 5 0z" fill="#fff"/></svg>Tamberlin Avenue, Larkfield, WR 3418</div>
    <div class="contact"><svg width="4" height="4" viewBox="0 0 10 10"><rect x="0" y="2" width="10" height="6.5" fill="#fff"/><path d="M0 2l5 3.5L10 2" stroke="var(--bottle)" fill="none"/></svg>willowmere-p.school@cbs.edu.au</div>
    <div class="contact"><svg width="4" height="4" viewBox="0 0 10 10"><path d="M2 0l2 2.5-1.2 1.4a6 6 0 0 0 3.3 3.3L7.5 6 10 8 8.5 10C4 10 0 6 0 1.5z" fill="#fff"/></svg>02 7316 4859</div>
  </div>
  <div class="card-address">TEVARN Provider Code: 00731K</div>
</section>

<!-- Letterhead -->
<section class="piece letterhead" aria-label="Letterhead">
  <svg class="shape" width="293" height="416" viewBox="0 0 293 416" aria-hidden="true">
    <path d="M0,350 H122 C150,350 152,358 180,358 H293 V374 H205 C178,374 172,416 145,416 H0 Z" fill="var(--bottle)"/>
  </svg>
  <div class="mark on-white"><span class="mark-square"></span>Willowmere Heights</div>
  <header class="masthead">
    <h1>WILLOWMERE HEIGHTS PUBLIC SCHOOL</h1>
    <p>Coastal Board of Schooling | TEVARN Provider Code: 00731K</p>
  </header>
  <div class="head-rule"></div>
  <div class="letter-date">Date: 10 September, 2019</div>
  <div class="letter-body">
    <p>Thank you for your continued support of our school community. This letter sets out the key dates for the coming term and the events planned for our students and families.</p>
    <p>Our staff have prepared a full program of learning, sport and creative activities. We welcome parents to join us at assemblies and open classroom days throughout the term, and we value your involvement.</p>
    <p>Please review the attached calendar and return any consent forms to the front office by the end of the month. Our office team is happy to help with any questions.</p>
    <p>Excursions, swimming lessons and the annual book fair will run in the second half of term. Further details and costs will be shared in the weekly newsletter.</p>
    <p>We look forward to another rewarding term together.</p>
    <p>Kind regards,</p>
  </div>
  <div class="signoff">
    <div class="signature">Signature</div>
    <div class="signer">RENA CALDWELL</div>
    <div class="signer-role">Manager</div>
  </div>
  <div class="contacts">
    <div class="contact"><svg width="5" height="5" viewBox="0 0 10 10"><path d="M5 0a3.6 3.6 0 0 0-3.6 3.6C1.4 6.5 5 10 5 10s3.6-3.5 3.6-6.4A3.6 3.6 0 0 0 5 0z" fill="#fff"/></svg>Tamberlin Avenue, Larkfield, WR 3418</div>
    <div class="contact"><svg width="5" height="5" viewBox="0 0 10 10"><rect x="0" y="2" width="10" height="6.5" fill="#fff"/><path d="M0 2l5 3.5L10 2" stroke="var(--bottle)" fill="none"/></svg>willowmere-p.school@cbs.edu.au</div>
    <div class="contact"><svg width="5" height="5" viewBox="0 0 10 10"><path d="M2 0l2 2.5-1.2 1.4a6 6 0 0 0 3.3 3.3L7.5 6 10 8 8.5 10C4 10 0 6 0 1.5z" fill="#fff"/></svg>02 7316 4859</div>
  </div>
  <div class="footer-board">Coastal Board of Schooling | TEVARN Provider Code: 00731K</div>
</section>

<!-- Compliments slip -->
<section class="piece slip" aria-label="With compliments slip">
  <svg class="shape" width="328" height="164" viewBox="0 0 328 164" aria-hidden="true">
    <path d="M0,91 H140 C172,91 178,117 212,117 H328 V164 H0 Z" fill="var(--bottle)"/>
  </svg>
  <div class="mark on-white"><span class="mark-square"></span>Willowmere Heights</div>
  <div class="write-lines"><span></span><span></span><span></span></div>
  <div class="school-name">WILLOWMERE HEIGHTS PUBLIC SCHOOL</div>
  <div class="contacts">
    <div class="contact"><svg width="5" height="5" viewBox="0 0 10 10"><path d="M5 0a3.6 3.6 0 0 0-3.6 3.6C1.4 6.5 5 10 5 10s3.6-3.5 3.6-6.4A3.6 3.6 0 0 0 5 0z" fill="#fff"/></svg>Tamberlin Avenue, Larkfield, WR 3418</div>
    <div class="contact"><svg width="5" height="5" viewBox="0 0 10 10"><rect x="0" y="2" width="10" height="6.5" fill="#fff"/><path d="M0 2l5 3.5L10 2" stroke="var(--bottle)" fill="none"/></svg>willowmere-p.school@cbs.edu.au</div>
    <div class="contact"><svg width="5" height="5" viewBox="0 0 10 10"><path d="M2 0l2 2.5-1.2 1.4a6 6 0 0 0 3.3 3.3L7.5 6 10 8 8.5 10C4 10 0 6 0 1.5z" fill="#fff"/></svg>02 7316 4859</div>
  </div>
  <div class="board">Coastal Board of Schooling<br>TEVARN Provider Code: 00731K</div>
</section>

<!-- Envelope back -->
<section class="piece envelope" aria-label="Envelope back">
  <svg class="shape" width="329" height="164" viewBox="0 0 329 164" aria-hidden="true">
    <path d="M0,0 H329 V12 L300,38 Q294,44 284,44 H45 Q35,44 29,38 L0,12 Z" fill="var(--bottle)"/>
  </svg>
  <div class="mark on-white"><span class="mark-square"></span>Willowmere Heights</div>
</section>

</body>
</html>
```